Creation of a book cover
Size : 14 x 20,5 cm (+ 5 mm bleed area at the top, bottom and right areas)
The Title is a French sentence which means “The heron dreaming on the cold roof of this empty station”. It’s a surrealistic title which has no link to the story.
AUTHOR : Mathieu Vorlange
TITLE : "Le héron rêvant sur le toit froid de cette gare vide »
PUBLISHER (AT THE BOTTOM OF THE PAGE) : Editions Parvenche
I send a PDF file with the kind of cover we have imagine, but you can propose something different. The glass and the fly can of course be used.

```html
<!DOCTYPE html>
<html lang="fr">
<head>
<meta charset="utf-8">
<title>Le héron rêvant sur le toit froid de cette gare vide — Couverture</title>
<link rel="stylesheet" href="https://fonts.googleapis.com/css2?family=Gochi+Hand&family=Montserrat:wght@400;500&family=Permanent+Marker&display=block">
<style>
  :root {
    --backdrop: #e6e6e8;
    --cover-red: #b00f0f;
    --band-yellow: #f2d21c;
    --band-shade: #c9a812;
    --ink-dark: #1a1a1a;
    --paper: #f4f4f4;
    --title-white: #f7f7f7;
    --subtitle-yellow: #f0dd4a;
    --foot-black: #0c0c0c;
    --glass-light: #e9edef;
    --glass-mid: #c6cfd4;
    --glass-deep: #9eabb2;
  }
  html, body {
    margin: 0;
    width: 1200px;
    height: 1200px;
    overflow: hidden;
    background: var(--backdrop);
  }
  .book-cover {
    position: absolute;
    left: 320px;
    top: 190px;
    width: 560px;
    height: 820px;
    background: var(--paper);
    overflow: hidden;
    box-shadow: 0 10px 30px rgba(0,0,0,0.15);
  }
  .cover-illustration {
    position: absolute;
    left: 165px;
    top: 470px;
    width: 230px;
    height: 230px;
    border-radius: 18px 18px 28px 28px;
    background: linear-gradient(180deg, var(--glass-light) 0%, var(--glass-mid) 55%, var(--glass-deep) 100%);
    box-shadow: -14px 14px 26px rgba(0,0,0,0.12);
    transform: rotate(-6deg);
  }
  .cover-shapes {
    position: absolute;
    inset: 0;
  }
  .author-band {
    position: absolute;
    left: 0;
    top: 42px;
    width: 100%;
    height: 54px;
    background: linear-gradient(90deg, var(--band-shade), var(--band-yellow) 30%);
    display: flex;
    align-items: center;
    justify-content: center;
  }
  .author-name {
    margin: 0;
    font-family: "Montserrat", sans-serif;
    font-weight: 500;
    font-size: 31px;
    letter-spacing: 1px;
    text-transform: uppercase;
    color: var(--ink-dark);
  }
  .book-title {
    position: absolute;
    left: 40px;
    right: 30px;
    top: 118px;
    margin: 0;
    font-weight: normal;
  }
  .title-main {
    display: block;
    font-family: "Permanent Marker", cursive;
    font-size: 84px;
    line-height: 1.05;
    color: var(--title-white);
    text-transform: uppercase;
  }
  .title-rest {
    display: block;
    margin-top: 10px;
    padding-left: 30px;
    font-family: "Gochi Hand", cursive;
    font-size: 38px;
    line-height: 1.05;
    color: var(--subtitle-yellow);
  }
  .publisher-name {
    position: absolute;
    left: 0;
    right: 0;
    bottom: 28px;
    margin: 0;
    text-align: center;
    font-family: "Montserrat", sans-serif;
    font-size: 21px;
    color: #ffffff;
  }
</style>
</head>
<body>
  <main class="book-cover">
    <div class="cover-illustration" role="img"
         aria-label="Illustration : un verre d'eau légèrement incliné, un insecte posé à l'intérieur"></div>

    <svg class="cover-shapes" width="560" height="820" viewBox="0 0 560 820" aria-hidden="true">
      <path class="red-field" fill="var(--cover-red)"
        d="M0 0 H560 V420 C530 436 505 410 470 428 C440 444 410 420 380 434 C350 448 320 424 290 438
           C260 452 240 428 210 442 C180 454 150 432 120 444 C95 454 80 432 60 422 C40 412 20 432 0 424 Z"/>
      <circle cx="470" cy="470" r="4" fill="var(--cover-red)"/>
      <circle cx="500" cy="500" r="3" fill="var(--cover-red)"/>
      <circle cx="440" cy="520" r="2.5" fill="var(--cover-red)"/>
      <circle cx="90" cy="478" r="3" fill="var(--cover-red)"/>
      <path class="black-foot" fill="var(--foot-black)"
        d="M0 730 C30 720 50 740 80 728 C110 716 130 742 170 734 C210 726 240 712 280 726
           C320 740 350 718 390 730 C430 742 460 722 500 734 C525 742 545 728 560 732 V820 H0 Z"/>
    </svg>

    <div class="author-band">
      <p class="author-name">Mathieu Vorlange</p>
    </div>

    <h1 class="book-title">
      <span class="title-main">Le héron</span>
      <span class="title-rest">rêvant sur le toit froid<br>de cette gare vide</span>
    </h1>

    <p class="publisher-name">Editions Parvenche</p>
  </main>
</body>
</html>
```